Warranty Card Design for Mattress Brand

We would like to design a warranty card for our mattresses,
it consists of 2 pages in one card (front and back) to be neatly showing our warranty details/text , our logo , our website, address and telephone clearly.

Target Market(s)

household

Font styles to use
Serif
Script

Colors
3277b5
33a6d7
85cae6
0492cd
3176b5
0355a3
85abd2
cee9f5
85acd3

Requirements
Must have
• a nice warranty logo
Nice to have
• a nice warranty logo with a neat text and clear layout, colors have to be related to the logo

```html
<!DOCTYPE html>
<html lang="en">
<head>
<meta charset="utf-8">
<title>Duskrest Mattress Warranty Card</title>
<link href="https://fonts.googleapis.com/css2?family=Arimo:wght@400&family=Cormorant+Garamond:wght@500&display=swap" rel="stylesheet">
<style>
  :root {
    --stage: #b4b4b4;
    --night-deep: #0b1f5e;
    --night-mid: #0d3a8a;
    --night-glow: #1f7fc0;
    --ink-white: #ffffff;
    --ink-blue: #0355a3;
    --brand-blue: #3277b5;
    --paper: #ffffff;
  }
  * { margin: 0; padding: 0; box-sizing: border-box; }
  html, body { width: 1200px; height: 1013px; overflow: hidden; }
  body {
    background: var(--stage);
    font-family: "Arimo", Arial, sans-serif;
    position: relative;
  }
  .card { position: absolute; overflow: hidden; }

  /* Front */
  .card-front {
    left: 40px; top: 59px; width: 928px; height: 415px;
    color: var(--ink-white);
  }
  .night-sky {
    position: absolute; inset: 0;
    background:
      radial-gradient(ellipse 55% 70% at 28% 55%, rgba(40,150,210,.55), transparent 70%),
      radial-gradient(ellipse 50% 60% at 80% 15%, rgba(30,110,190,.45), transparent 70%),
      linear-gradient(160deg, var(--night-mid) 0%, var(--night-deep) 55%, #13256e 100%);
  }
  .brand-frame {
    position: absolute; left: 53px; top: 72px; width: 245px; height: 242px;
    border: 4px solid var(--ink-white);
    display: flex; align-items: center; justify-content: center;
  }
  .brand-name {
    font-family: "Cormorant Garamond", Georgia, serif;
    font-weight: 500; font-size: 54px; letter-spacing: 1px;
    color: var(--ink-white);
  }
  .warranty-terms {
    position: absolute; left: 408px; top: 51px; width: 462px;
    font-size: 12.2px; line-height: 15.6px;
  }
  .warranty-terms li { list-style: none; padding-left: 10px; text-indent: -10px; }
  .warranty-terms li.term-point::before { content: "- "; }
  .warranty-terms li.term-heading { padding-left: 0; text-indent: 0; }
  .front-footer {
    position: absolute; top: 361px; left: 53px; right: 0;
    font-size: 13.5px; line-height: 18px;
  }
  .front-footer .phone { position: absolute; left: 355px; top: 18px; }
  .front-footer .web { position: absolute; left: 622px; top: 18px; }

  /* Back */
  .card-back {
    left: 226px; top: 512px; width: 931px; height: 416px;
    background: var(--paper); color: var(--ink-blue);
    font-size: 11.6px; line-height: 15.3px;
  }
  .sky-band {
    position: absolute; left: 0; top: 0; width: 100%; height: 37px;
    background: linear-gradient(90deg, var(--night-deep), var(--night-mid) 50%, #12307a);
  }
  .welcome { position: absolute; left: 32px; top: 59px; width: 880px; }
  .care { position: absolute; left: 32px; top: 164px; width: 880px; }
  .care li { list-style: none; }
  .care li::before { content: "-  "; }
  .record-fields { position: absolute; left: 32px; top: 267px; display: flex; }
  .record-fields span:nth-child(1) { width: 173px; }
  .record-fields span:nth-child(2) { width: 190px; }
  .back-contact { position: absolute; left: 32px; top: 323px; }
  .back-brand {
    position: absolute; left: 640px; top: 322px;
    font-family: "Cormorant Garamond", Georgia, serif;
    font-weight: 500; font-size: 44px; line-height: 1;
    color: var(--brand-blue);
  }
</style>
</head>
<body>

<section class="card card-front">
  <div class="night-sky" role="img" aria-label="Deep blue starry night sky background"></div>
  <div class="brand-frame"><span class="brand-name">Duskrest</span></div>
  <ul class="warranty-terms">
    <li class="term-heading">This limited Mattress Warranty applies to the following Defects:</li>
    <li class="term-point">Coils or wires that are broken or piercing through fabric.</li>
    <li class="term-point">Sagging, that measures 3cm or greater (being properly measured) only if the mattress has been continuously supported by appropriate and solid foundation</li>
    <li class="term-heading">This limited Mattress Warranty does not cover the following:</li>
    <li class="term-point">Comfort preference</li>
    <li class="term-point">Fabric Stains, soiling or burns</li>
    <li class="term-point">Body impressions of less than 3cm</li>
    <li class="term-point">Damage to the mattress due to abuse</li>
    <li class="term-point">Bent Perimeter border rods due to moving or bending the mattress</li>
    <li class="term-point">Size allowance of +/- 2cm</li>
    <li class="term-point">Bed Bugs and Dust Mites</li>
    <li class="term-point">Mattress Odor: as in any upholstery, new mattress may have odor that will fade with time</li>
    <li class="term-point">For Latex and Memory Foam mattresses: normal change in softness and recovery time in these materials with time. This does not affect the relieving qualities of these mattresses.</li>
    <li class="term-point">Transportation and Inspection Costs</li>
  </ul>
  <div class="front-footer">
    <p>Halim Farid and Sons<br>Cedar Heights, Mill Road, Zahle, Lebanon</p>
    <p class="phone">+961 1 555 010</p>
    <p class="web">www.halimfaridsons.com</p>
  </div>
</section>

<section class="card card-back">
  <div class="sky-band" role="img" aria-label="Thin starry night sky band"></div>
  <div class="welcome">
    <p>Congratulations on your new DUSKREST mattress.</p>
    <p>We always strive to provide you with the most comfortable and healthy sleep by offering you the highest product quality and durability.</p>
    <p>Our company was awarded the ISO 9001 accreditation certificate for the quality of its Mattress Production.</p>
    <p>By implementing the ISO 9001 quality management system, we assure our customers that the products and the services we provide will meet their expectations.</p>
    <p>Our products are guaranteed against defects in workmanship and material. In case of defect, we shall repair or replace, at our discretion, the defective component.</p>
    <p>Please keep this card in a safe place. Should you face any problems, please contact our service department</p>
  </div>
  <div class="care">
    <p>To ensure you get maximum comfort and support, please follow the following instructions:</p>
    <ul>
      <li>Make sure the bed base foundation is in good condition and well ventilated.</li>
      <li>Turn/Flip your mattress every 3 months to maximize its comfort and lifespan.</li>
      <li>Avoid exposing the mattress to the sun; air it in a passage area instead.</li>
      <li>In case of possibility of liquids dripping on the mattress, consider covering it with a mattress protection pad.</li>
      <li>Do not worry if the mattress feels slightly firmer than anticipated within weeks of usage, the interior will soften and initial stiffness will be removed.</li>
    </ul>
  </div>
  <div class="record-fields">
    <span>Invoice Number</span><span>Warranty Period</span><span>Date</span>
  </div>
  <div class="back-contact">
    <p>Halim Farid and Sons</p>
    <p>Cedar Heights, Mill Road, Zahle, Lebanon</p>
    <p>+961 1 555 010</p>
    <p>www.halimfaridsons.com</p>
  </div>
  <div class="back-brand">Duskrest</div>
</section>

</body>
</html>
```